mobile app design: app provides timely Natural gas pipeline information (similar to weather, etc)

we are going to create and publish an app in all the three markets.( android, ios,windows). we have wire framed mostly all the screens. the designers are to provide the layout, design & background. The following are the most important things.

1. the app's target audience are guys working in the natural gas industry in the US.
2. the app provides the customer with latest pipeline information
3. the trial version is free and will provide information about one pipeline
4. slides 1 to 5 are trial version slides.
5. slides 6 onwards the customer chooses.
6. the final product is displayed in a grid.
7. the app will be developed using html5 and css3.
8. customer will pay per pipeline for the information. ( in app payment)
9 there are similiar ( complementary) products which provide weekly storage data at vexlo mart and quorbit app store.
10. i have attached the pdf document of the wireframe.
11.i have attached the logo
12. no name has been thought out yet.

Hi guys

I have a main question for the designer community .

1. is it possible to combine some of the pages ( screens  ) into one or two. use your gut feel. if not it is ok.

2. check out the flow, the color, the background , the font and the font size. it should be pleasing.

thanx

Tomek

Natural Gas

```html
<!DOCTYPE html>
<html lang="en">
<head>
<meta charset="utf-8">
<title>Pipeline Feed</title>
<link href="https://fonts.googleapis.com/css2?family=Marcellus+SC&family=Kalam:wght@400&display=swap" rel="stylesheet">
<style>
  :root {
    --sky: #88aad4;
    --stripe: #ffffff;
    --navy: #0b4c9c;
    --tab-frame: #1f56a6;
    --tab-plate: #5f86c6;
    --tab-edge: #9db8e0;
    --panel: rgba(40, 88, 165, 0.55);
    --grid-bg: #1f56a8;
    --grid-line: #16448a;
    --cell-text: #ffffff;
    --scroll-track: #1a4c9a;
    --scroll-thumb: #b7cbe8;
  }
  * { box-sizing: border-box; margin: 0; padding: 0; }
  html, body { width: 734px; height: 1200px; overflow: hidden; background: var(--sky); }
  .screen { position: relative; width: 734px; height: 1200px; overflow: hidden; background: var(--sky); }
  .stripe { position: absolute; top: 0; height: 1080px; background: var(--stripe); }
  .stripe--left { left: 237px; width: 45px; }
  .stripe--right { left: 471px; width: 66px; }
  .backdrop-wave { position: absolute; left: 0; top: 0; width: 734px; height: 1200px; }

  .tabs { position: absolute; top: 370px; left: 42px; width: 666px; height: 84px; }
  .tab {
    position: absolute; top: 0; height: 84px; background: var(--tab-frame);
    border-radius: 6px; padding: 10px;
  }
  .tab span {
    display: flex; align-items: center; justify-content: center; height: 100%;
    background: var(--tab-plate); border: 2px solid var(--tab-edge); border-radius: 4px;
    font-family: "Marcellus SC", serif; color: #fff; font-size: 22px; letter-spacing: 2px;
    text-align: center; line-height: 1;
  }
  .tab--latest { left: 0; width: 217px; }
  .tab--latest span { width: 180px; }
  .tab--older { left: 224px; width: 213px; }
  .tab--older span { width: 186px; }
  .tab--add { left: 448px; width: 218px; }
  .tab--add span { width: 186px; font-size: 19px; }

  .feed-panel {
    position: absolute; top: 468px; left: 44px; width: 666px; height: 394px;
    background: var(--panel); border-radius: 18px;
  }
  .feed-table {
    position: absolute; top: 24px; left: 27px; width: 566px; height: 344px;
    background: var(--grid-bg); border-radius: 16px; overflow: hidden;
    display: grid; grid-template-columns: 112px 136px 149px 169px;
    grid-template-rows: 64px repeat(5, 48px) 40px;
  }
  .feed-table > div {
    border-right: 3px solid var(--grid-line); border-bottom: 3px solid var(--grid-line);
    color: var(--cell-text); display: flex; align-items: center; padding-left: 14px;
  }
  .feed-table > div:nth-child(4n) { border-right: none; }
  .head { font-family: "Marcellus SC", serif; font-size: 17px; letter-spacing: 1.5px; }
  .cell { font-family: "Kalam", cursive; font-style: italic; font-size: 23px; }
  .feed-table .spacer { border-bottom: none; }

  .scrollbar {
    position: absolute; top: 18px; left: 614px; width: 25px; height: 350px;
    background: var(--scroll-track); border: 2px solid #0d3a78; border-radius: 8px;
  }
  .scrollbar .thumb {
    position: absolute; top: 88px; left: 2px; width: 17px; height: 84px;
    background: var(--scroll-thumb); border-radius: 6px;
  }

  .next-button { position: absolute; left: 261px; top: 922px; width: 188px; height: 188px; }
</style>
</head>
<body>
<main class="screen">
  <div class="stripe stripe--left"></div>
  <div class="stripe stripe--right"></div>

  <svg class="backdrop-wave" viewBox="0 0 734 1200" aria-hidden="true">
    <path d="M0 1070 Q 420 1030 734 882 L734 1200 L0 1200 Z" fill="#ffffff"/>
    <path d="M0 1078 Q 420 1040 734 892 L734 1200 L0 1200 Z" fill="var(--navy)"/>
  </svg>

  <nav class="tabs">
    <div class="tab tab--latest"><span>Latest</span></div>
    <div class="tab tab--older"><span>Older</span></div>
    <div class="tab tab--add"><span>Add more<br>pipelines</span></div>
  </nav>

  <section class="feed-panel">
    <div class="feed-table">
      <div class="head">Region</div><div class="head">Pipeline</div><div class="head">Gasday</div><div class="head">Postingtime</div>
      <div class="cell">data1</div><div class="cell">data2</div><div class="cell">data3</div><div class="cell">data4</div>
      <div class="cell">data11</div><div class="cell">data21</div><div class="cell">data31</div><div class="cell">data41</div>
      <div class="cell">data12</div><div class="cell">data22</div><div class="cell">data32</div><div class="cell">data42</div>
      <div class="cell">data13</div><div class="cell">data23</div><div class="cell">data33</div><div class="cell">data43</div>
      <div class="cell">data14</div><div class="cell">data24</div><div class="cell">data34</div><div class="cell">data44</div>
      <div class="spacer"></div><div class="spacer"></div><div class="spacer"></div><div class="spacer"></div>
    </div>
    <div class="scrollbar"><div class="thumb"></div></div>
  </section>

  <svg class="next-button" viewBox="0 0 188 188" role="img" aria-label="Next">
    <circle cx="94" cy="94" r="92" fill="rgba(150,180,225,0.55)" stroke="#c9d8ee" stroke-width="3"/>
    <circle cx="94" cy="94" r="68" fill="#1f5cb0" stroke="#8fb0dc" stroke-width="3"/>
    <path d="M70 52 L118 94 L70 136 L84 94 Z" fill="#7fa2d6"/>
    <path d="M84 60 L124 94 L84 128 L96 94 Z" fill="#a9c2e6"/>
  </svg>
</main>
</body>
</html>
```